Webdesign Hauskranken- und Tagespflege „Am Lindenhof“
Zielgruppe
Die Hauskranken- und Tagespflege „Am Lindenhof“ in Chemnitz ist ein unabhängiges, privat geführtes Unternehmen im Bereich der ambulanten und teilstationären Kranken- und Seniorenpflege. Seit der Gründung am 1. Mai 2007 stehen wir für eine zuverlässige, individuelle und herzliche Betreuung unserer Klientinnen und Klienten.
Das Team ist ein engagiertes Pflegeteam und auf über 35 qualifizierte Mitarbeiterinnen und Mitarbeiter angewachsen. Gemeinsam setzen wir uns täglich dafür ein, Menschen mit Pflegebedarf eine bestmögliche Versorgung und ein hohes Maß an Lebensqualität zu ermöglichen.
Unsere Firmenphilosophie basiert auf Wertschätzung, Vertrauen und Respekt – sowohl im Umgang mit unseren Klientinnen und Klienten sowie deren Angehörigen als auch innerhalb unseres Teams. Eine persönliche, einfühlsame und fachlich kompetente Betreuung steht für uns an erster Stelle.
Ob Grundpflege oder Behandlungspflege – bei uns sind Sie in guten Händen. Wir begleiten unsere Klientinnen und Klienten mit Fürsorge, Fachkompetenz und Herz und unterstützen sie dabei, ihren Alltag so selbstbestimmt wie möglich zu gestalten.
Gleichzeitig entlasten wir Angehörige, Freunde und Bekannte, indem wir ihnen Sicherheit geben und Freiräume schaffen. So bleibt mehr Zeit für gemeinsame, unbeschwerte Momente mit den Menschen, die ihnen am Herzen liegen.
Unsere Tagespflege bietet Platz für 18 Gäste. Der große Aufenthaltsraum mit offener Küche lädt zum gemütlichen Beisammensein ein. In unserem Ruheraum können sich unsere Gäste bei Bedarf zurückziehen und sich ausruhen, auch Therapien (Logopädie, Ergotherapie, Physiotherapie…) werden darin durchgeführt. Der Aufenthaltsraum ist zum Teil eingerichtet wie eine gemütliche Wohnstube, ihre Einrichtung erinnert an frühere Zeiten. Gemütliche Ruhesessel laden zum Entspannen ein.
Der persönliche Kontakt und das Vertrauen unserer Patientinnen und Patienten bilden dabei st..
Aufgabenstellung
Ziele des Relaunchs:
modernes, freundliches und barrierearmes Design
klare Benutzerführung für Senioren und Angehörige
Hinweis zum Rückrufservice
Notfallnummer dauerhaft sichtbar
schnelle Kontaktaufnahme (Telefon, Rückruf, Kontaktformular)
bessere Auffindbarkeit bei Google (SEO)
Vertrauen durch authentische Bilder, Teamvorstellung und Bewertungen

```html
<!DOCTYPE html>
<html lang="de">
<head>
<meta charset="utf-8">
<title>Hauskranken- und Tagespflege „Am Lindenhof“</title>
<link href="https://fonts.googleapis.com/css2?family=Libre+Baskerville:wght@400;700&family=Montserrat:wght@400;500;600;700&family=Kaushan+Script&display=swap" rel="stylesheet">
<style>
:root{
  --teal:#0f4c57;
  --teal-dark:#0b3a44;
  --yellow:#f6b800;
  --cream:#fbf7f1;
  --ink:#1c1c1c;
  --muted:#4a4a4a;
  --white:#ffffff;
}
*{box-sizing:border-box;margin:0;padding:0}
html,body{width:1200px;height:4100px;overflow:hidden}
body{background:var(--cream);font-family:"Montserrat",sans-serif;color:var(--ink);position:relative}
.abs{position:absolute}
.serif{font-family:"Libre Baskerville",serif;font-weight:700}
.script{font-family:"Kaushan Script",cursive}
.photo{position:absolute}

/* top bar */
.topbar{position:absolute;left:0;top:0;width:1200px;height:48px;background:var(--teal-dark);color:#fff;font-size:16px;display:flex;align-items:center;padding:0 30px;justify-content:space-between}
.topbar .hours{display:flex;align-items:center;gap:12px}
.topbar .hotline{color:var(--yellow);font-weight:600;display:flex;align-items:center;gap:10px;font-size:17px}

/* header */
.brand{left:60px;top:60px;display:flex;align-items:center;gap:10px}
.brand .dot{width:22px;height:22px;border-radius:50%;background:var(--yellow)}
.brand span{font-size:16px;font-weight:700;color:var(--teal);width:110px;line-height:1.2}
.nav{left:242px;top:88px;display:flex;gap:56px;font-size:16px;font-weight:500}
.nav-phone{left:936px;top:67px;width:239px;height:63px;border:2px solid var(--teal);border-radius:6px;display:flex;align-items:center;gap:18px;padding-left:18px;font-size:17px;color:var(--teal-dark);font-weight:500;line-height:1.2}

/* hero */
.hero-title{left:56px;top:262px;font-size:52px;line-height:61px;color:var(--ink)}
.hero-title em{font-style:normal;color:var(--teal)}
.hero-lead{left:60px;top:452px;font-size:17px;line-height:27px;font-weight:500;width:360px}
.btn{position:absolute;display:flex;align-items:center;gap:12px;border-radius:5px;font-size:13px;font-weight:600}
.btn-yellow{background:var(--yellow);color:var(--ink)}
.btn-outline{border:2px solid var(--teal);color:var(--teal);background:#fff}

/* stats */
.stat{position:absolute;display:flex;align-items:center;gap:18px}
.stat .ico{width:92px;height:92px;border-radius:50%;background:var(--yellow);display:flex;align-items:center;justify-content:center}
.stat .num{font-size:50px;font-weight:600;line-height:1}
.stat .lbl{font-size:16px;font-weight:500;line-height:24px}

/* services */
.section-title{font-size:38px;text-align:center;width:1200px;left:0}
.card{position:absolute;top:1076px;width:557px;height:422px;background:#fff;border-radius:14px;overflow:hidden;box-shadow:0 2px 10px rgba(0,0,0,.05)}
.card .pic{position:absolute;left:0;top:0;width:278px;height:422px}
.card .body{position:absolute;left:306px;top:30px;width:240px}
.card .ic{width:58px;height:58px;border-radius:50%;background:var(--teal);display:flex;align-items:center;justify-content:center}
.card h3{font-size:24px;color:var(--teal);margin-top:30px}
.card p{font-size:14px;line-height:24px;margin-top:14px}
.card ul{list-style:none;font-size:13px;line-height:24px;margin-top:22px}
.card ul li::before{content:"✓";margin-right:12px}
.card .btn{position:relative;margin-top:26px;width:171px;height:38px;padding-left:16px;font-size:13px}

/* values */
.values{left:0;top:1550px;width:1200px;height:466px;background:var(--teal-dark);color:#fff}
.values h2{position:absolute;left:83px;top:98px;font-size:37px;line-height:56px}
.values h2 b{color:var(--yellow);font-weight:700}
.values p.lead{position:absolute;left:83px;top:216px;font-size:19px;line-height:30px}
.value{position:absolute;top:118px;width:220px;text-align:center}
.value h3{font-size:22px;margin-top:22px}
.value p{font-size:11px;line-height:19px;margin-top:20px}

/* day */
.day-title{left:46px;top:2060px;font-size:48px;color:var(--teal)}
.day-sub{left:46px;top:2136px;font-size:16px;font-weight:500}
.tl-line{left:70px;top:2210px;width:2px;height:290px;background:var(--teal)}
.tl{position:absolute;left:46px;display:flex;gap:20px}
.tl .ic{width:48px;height:48px;border-radius:50%;background:var(--teal);flex:none;display:flex;align-items:center;justify-content:center}
.tl h4{font-family:"Libre Baskerville",serif;font-size:17px;color:var(--teal)}
.tl .t{font-size:14px;font-weight:500;margin-top:4px}
.tl .s{font-size:10px;margin-top:4px;line-height:13px;width:250px}
.fahr{left:530px;top:2346px;width:214px;height:214px;border-radius:50%;background:var(--yellow);color:#fff;text-align:center;display:flex;flex-direction:column;justify-content:center}

/* team */
.team-title{left:40px;top:2640px;font-size:27px;line-height:40px;color:var(--teal)}
.team-lead{left:40px;top:2722px;font-size:14px;line-height:23px;width:260px}
.member{position:absolute;top:2648px;width:201px;height:296px;background:#fff;border-radius:8px;overflow:hidden;text-align:center;box-shadow:0 2px 10px rgba(0,0,0,.05)}
.member .pic{height:201px;margin:0}
.member h4{font-family:"Libre Baskerville",serif;font-size:14px;color:var(--teal);margin-top:14px}
.member .bar{width:26px;height:2px;background:var(--yellow);margin:8px auto}
.member p{font-size:11px;color:var(--teal);line-height:17px}

/* thanks */
.thanks-title{left:70px;top:3045px;font-size:37px;color:var(--teal)}
.quote-mark{left:64px;top:3100px;font-family:"Libre Baskerville",serif;font-size:110px;color:var(--yellow);line-height:1}
.thanks-text{left:162px;top:3112px;font-size:18px;line-height:23px;font-weight:500}
.thanks-script{left:162px;top:3207px;font-size:34px;color:var(--teal)}
.thanks-name{left:162px;top:3266px;font-size:16px;font-weight:600}
.thanks-name small{display:block;font-size:11px;font-style:italic;font-weight:500}

/* contact */
.ask-title{left:60px;top:3360px;font-size:40px;line-height:58px}
.ask-title em{font-style:normal;color:var(--teal);display:block}
.ask-lead{left:60px;top:3486px;font-size:17px;line-height:22px;font-weight:500}
.ccard{position:absolute;top:3560px;width:200px;height:101px;background:#fff;border-left:4px solid var(--yellow);border-radius:8px;display:flex;align-items:center;gap:14px;padding-left:14px;box-shadow:0 2px 10px rgba(0,0,0,.06)}
.ccard .ic{width:40px;height:40px;border-radius:50%;background:#eef1f1;flex:none;display:flex;align-items:center;justify-content:center}
.ccard b{font-size:12px;display:block}
.ccard span{font-size:13px;line-height:15px;display:block;margin-top:4px}
.ccard small{font-size:10px;display:block;margin-top:3px}

/* footer */
.f-name{left:146px;top:3772px;font-size:18px;line-height:27px;color:var(--teal)}
.f-brand{left:40px;top:3780px;width:90px;height:90px;border-radius:50%;border:2px solid var(--yellow)}
.f-script{left:150px;top:3882px;font-size:15px;line-height:25px;color:var(--teal)}
.f-small{left:146px;top:3948px;font-size:10px}
.f-col{position:absolute;top:3772px}
.f-col h5{font-family:"Libre Baskerville",serif;font-size:14px;color:var(--teal);font-weight:700}
.f-nav{list-style:none;font-size:11px;margin-top:22px}
.f-nav li{margin-bottom:26px}
.f-nav li::before{content:"·";margin-right:6px}
.f-row{display:flex;gap:14px;align-items:flex-start;margin-top:22px;font-size:11px;line-height:17px}
.f-row .ic{width:30px;height:30px;border-radius:50%;background:#eef1f1;flex:none;display:flex;align-items:center;justify-content:center}
.hotline-box{left:963px;top:3812px;width:162px;height:167px;border:2px solid var(--teal);border-radius:10px;text-align:center;color:var(--teal-dark);padding-top:28px}
.bottom{left:0;top:4018px;width:1200px;height:82px;background:var(--teal-dark);border-top:5px solid var(--yellow);color:#fff;font-size:11px;display:flex;align-items:center;justify-content:space-between;padding:0 44px}
.bottom nav{display:flex;gap:16px;align-items:center}
.bottom nav i{width:1px;height:20px;background:#fff}
</style>
</head>
<body>

<!-- Top bar -->
<div class="topbar">
  <div class="hours">
    <svg width="20" height="20" viewBox="0 0 20 20"><circle cx="10" cy="10" r="9" fill="#fff"/><path d="M10 4v6l4 2" stroke="#0b3a44" stroke-width="2" fill="none"/></svg>
    Mo - Do: 9:00 - 15:00 Uhr | Fr: 9:00 - 14:00 Uhr | und nach Vereinbarung
  </div>
  <div class="hotline">
    <svg width="26" height="26" viewBox="0 0 24 24"><path d="M6.6 10.8a15 15 0 006.6 6.6l2.2-2.2a1 1 0 011-.25 11.4 11.4 0 003.6.57 1 1 0 011 1V20a1 1 0 01-1 1A17 17 0 013 4a1 1 0 011-1h3.5a1 1 0 011 1c0 1.25.2 2.45.57 3.57a1 1 0 01-.25 1z" fill="#f6b800"/></svg>
    24h-Hotline 0371 / 4590120
  </div>
</div>

<!-- Header -->
<div class="abs brand"><div class="dot"></div><span>Am Lindenhof</span></div>
<nav class="abs nav"><span>Über uns</span><span>Hauskrankenpflege</span><span>Tagespflege</span><span>Team</span><span>Kontakt</span></nav>
<div class="abs nav-phone">
  <svg width="30" height="30" viewBox="0 0 24 24"><path d="M6.6 10.8a15 15 0 006.6 6.6l2.2-2.2a1 1 0 011-.25 11.4 11.4 0 003.6.57 1 1 0 011 1V20a1 1 0 01-1 1A17 17 0 013 4a1 1 0 011-1h3.5a1 1 0 011 1c0 1.25.2 2.45.57 3.57a1 1 0 01-.25 1z" fill="#0f4c57"/></svg>
  <div>24h-Hotline<br>0371 / 4590120</div>
</div>

<!-- Hero -->
<svg class="abs" style="left:440px;top:150px" width="760" height="570" viewBox="0 0 760 570">
  <defs><linearGradient id="heroG" x1="0" y1="0" x2="1" y2="1"><stop offset="0" stop-color="#cdb9a5"/><stop offset=".5" stop-color="#9aa7b0"/><stop offset="1" stop-color="#4f6f8e"/></linearGradient></defs>
  <path d="M30 0 H760 V420 C640 520 480 575 330 555 C140 525 0 400 10 220 C14 120 20 50 30 0Z" fill="url(#heroG)" role="img" aria-label="Foto: Pflegerin kümmert sich lächelnd um eine ältere Dame im Rollstuhl"/>
  <path d="M330 555 C520 560 680 480 760 380 V430 C680 520 520 570 330 555Z" fill="#f6b800"/>
</svg>
<h1 class="abs serif hero-title">Pflege,<br>die <em>Vertrauen</em><br>schafft.</h1>
<p class="abs hero-lead">Ambulante Hauskrankenpflege und Tagespflege in Chemnitz – persönlich, kompetent und mit Herz.</p>
<div class="btn btn-yellow" style="left:60px;top:555px;width:172px;height:45px;padding-left:16px">
  <svg width="18" height="18" viewBox="0 0 24 24"><path d="M6.6 10.8a15 15 0 006.6 6.6l2.2-2.2a1 1 0 011-.25 11.4 11.4 0 003.6.57 1 1 0 011 1V20a1 1 0 01-1 1A17 17 0 013 4a1 1 0 011-1h3.5a1 1 0 011 1c0 1.25.2 2.45.57 3.57a1 1 0 01-.25 1z" fill="#1c1c1c"/></svg>Kontakt aufnehmen</div>
<div class="btn btn-outline" style="left:272px;top:555px;width:194px;height:45px;padding-left:18px">
  <svg width="18" height="18" viewBox="0 0 24 24"><path d="M6.6 10.8a15 15 0 006.6 6.6l2.2-2.2a1 1 0 011-.25 11.4 11.4 0 003.6.57 1 1 0 011 1V20a1 1 0 01-1 1A17 17 0 013 4a1 1 0 011-1h3.5a1 1 0 011 1c0 1.25.2 2.45.57 3.57a1 1 0 01-.25 1z" fill="#0f4c57"/></svg>Rückruf anfordern</div>

<!-- Stats -->
<div class="stat" style="left:44px;top:775px">
  <div class="ico"><svg width="50" height="50" viewBox="0 0 24 24" fill="none" stroke="#0b3a44" stroke-width="1.4"><rect x="3" y="5" width="18" height="16" rx="2"/><path d="M3 10h18M8 3v4M16 3v4M9 15l2 2 4-4"/></svg></div>
  <div><div class="lbl" style="font-size:18px">Seit</div><div class="num">2007</div><div class="lbl">Für Sie da</div></div>
</div>
<div class="stat" style="left:347px;top:775px">
  <div class="ico"><svg width="54" height="54" viewBox="0 0 24 24" fill="none" stroke="#0b3a44" stroke-width="1.3"><circle cx="12" cy="8" r="3"/><circle cx="5.5" cy="10" r="2.2"/><circle cx="18.5" cy="10" r="2.2"/><path d="M7 19a5 5 0 0110 0zM1.5 19a4 4 0 016-3.4M22.5 19a4 4 0 00-6-3.4"/></svg></div>
  <div><div class="num">35+</div><div class="lbl">engagierte<br>Mitarbeiter</div></div>
</div>
<div class="stat" style="left:620px;top:775px">
  <div class="ico"><svg width="52" height="52" viewBox="0 0 24 24" fill="none" stroke="#0b3a44" stroke-width="1.3"><path d="M6 12V7a3 3 0 013-3h6a3 3 0 013 3v5"/><rect x="3" y="11" width="4" height="7" rx="1.5"/><rect x="17" y="11" width="4" height="7" rx="1.5"/><path d="M7 15h10M5 18v2M19 18v2"/></svg></div>
  <div><div class="num">18</div><div class="lbl">Tagespflegeplätze<br>für unsere Gäste</div></div>
</div>
<div class="stat" style="left:910px;top:775px">
  <div class="ico"><svg width="54" height="54" viewBox="0 0 24 24" fill="none" stroke="#0b3a44" stroke-width="1.3"><path d="M20 12a8 8 0 11-2.3-5.6M20 4v4h-4"/><text x="12" y="14.5" font-size="6.5" text-anchor="middle" fill="#0b3a44" stroke="none" font-family="Montserrat,sans-serif" font-weight="700">24h</text></svg></div>
  <div><div class="num">24h</div><div class="lbl">erreichbar – wenn<br>Sie uns brauchen</div></div>
</div>

<!-- Services -->
<h2 class="abs serif section-title" style="top:985px">Wie können wir Sie unterstützen?</h2>
<div class="card" style="left:27px">
  <div class="pic" style="background:linear-gradient(135deg,#e4dfd8,#b9c3cc 60%,#6d8aa4)" role="img" aria-label="Foto: Pflegerin misst einem älteren Herrn den Blutdruck"></div>
  <div class="body">
    <div class="ic"><svg width="32" height="32" viewBox="0 0 24 24" fill="none" stroke="#fff" stroke-width="1.5"><path d="M3 11l9-7 9 7M5 10v10h14V10"/><path d="M12 17s-3-1.8-3-3.6a1.6 1.6 0 013-.8 1.6 1.6 0 013 .8c0 1.8-3 3.6-3 3.6z"/></svg></div>
    <h3 class="serif">Hauskrankenpflege</h3>
    <p>Pflege und Unterstützung<br>in vertrauter Umgebung.</p>
    <ul><li>Grundpflege</li><li>Behandlungspflege</li><li>Hauswirtschaft</li><li>Unterstützung im Alltag</li></ul>
    <div class="btn btn-yellow">Mehr erfahren <svg width="22" height="14" viewBox="0 0 22 14" fill="none" stroke="#1c1c1c" stroke-width="1.8"><path d="M1 7h19M14 1l6 6-6 6"/></svg></div>
  </div>
</div>
<div class="card" style="left:616px">
  <div class="pic" style="background:linear-gradient(160deg,#c9a47a,#8c8a5a 50%,#5e6a52)" role="img" aria-label="Foto: Drei Senioren sitzen gemeinsam im Garten der Tagespflege"></div>
  <div class="body">
    <div class="ic"><svg width="32" height="32" viewBox="0 0 24 24" fill="none" stroke="#fff" stroke-width="1.4"><circle cx="8" cy="11" r="2"/><circle cx="16" cy="11" r="2"/><path d="M4 19a4 4 0 018 0M12 19a4 4 0 018 0M12 8s-2.5-1.4-2.5-3a1.3 1.3 0 012.5-.6 1.3 1.3 0 012.5.6c0 1.6-2.5 3-2.5 3z"/></svg></div>
    <h3 class="serif">Tagespflege</h3>
    <p>Gemeinsam den Tag verbringen, gut betreut und umsorgt.</p>
    <ul><li>Gemeinschaft</li><li>Aktivitäten</li><li>Fahrdienst</li><li>Frische Mahlzeiten</li></ul>
    <div class="btn btn-yellow">Mehr erfahren <svg width="22" height="14" viewBox="0 0 22 14" fill="none" stroke="#1c1c1c" stroke-width="1.8"><path d="M1 7h19M14 1l6 6-6 6"/></svg></div>
  </div>
</div>

<!-- Values -->
<section class="abs values">
  <h2 class="serif">Pflege mit <b>Respekt.</b><br>Betreuung mit <b>Herz.</b></h2>
  <p class="lead">Unsere Arbeit basiert auf Werten,<br>die für uns jeden Tag zählen.</p>
  <div class="value" style="left:495px">
    <svg width="84" height="80" viewBox="0 0 48 46" fill="none" stroke="#f6b800" stroke-width="1.6"><path d="M24 30s-8-5-8-10a4 4 0 018-1 4 4 0 018 1c0 5-8 10-8 10z"/><path d="M4 36l8-4h10a3 3 0 000-6h-6M44 10l-8 4H26a3 3 0 000 6"/></svg>
    <h3 class="serif">Respekt</h3>
    <p>Wir sehen den Menschen,<br>nicht nur den Pflegebedarf.<br>Wertschätzung und Verständnis<br>sind die Basis unseres Handelns.</p>
  </div>
  <div class="value" style="left:721px">
    <svg width="84" height="80" viewBox="0 0 48 46" fill="none" stroke="#f6b800" stroke-width="1.6"><path d="M2 18l8-6 6 2 6-3 6 2 6-2 8 6"/><path d="M10 12l-6 14 8 8M38 12l6 14-8 8M16 22l6 6 3-3 3 3 4-4M18 30l4 4 4-2"/></svg>
    <h3 class="serif">Vertrauen</h3>
    <p>Persönlicher Kontakt und<br>offene Kommunikation<br>schaffen Sicherheit für<br>Klienten und Angehörige.</p>
  </div>
  <div class="value" style="left:932px">
    <svg width="84" height="80" viewBox="0 0 48 46" fill="none" stroke="#f6b800" stroke-width="1.6"><circle cx="24" cy="18" r="14"/><circle cx="24" cy="18" r="9"/><path d="M20 18l3 3 5-6M16 30l-4 12 6-3 3 5 3-10M32 30l4 12-6-3-3 5-3-10"/></svg>
    <h3 class="serif">Kompetenz</h3>
    <p>Qualifizierte Pflege,<br>kontinuierliche Weiterbildung<br>und Erfahrung seit 2007<br>für Ihre bestmögliche Versorgung.</p>
  </div>
</section>

<!-- A day with us -->
<svg class="abs" style="left:460px;top:2016px" width="740" height="580" viewBox="0 0 740 580">
  <defs><linearGradient id="dayG" x1="0" y1="0" x2="1" y2="0"><stop offset="0" stop-color="#d8c7b3"/><stop offset=".5" stop-color="#b59a80"/><stop offset="1" stop-color="#d9d3cc"/></linearGradient></defs>
  <path d="M40 0 H740 V470 C640 540 500 570 360 560 C160 540 40 420 20 260 C10 160 20 60 40 0Z" fill="url(#dayG)" role="img" aria-label="Foto: Pflegerin und Seniorin trinken gemeinsam Tee"/>
  <path d="M360 560 C520 566 660 510 740 440 V490 C660 550 520 578 360 560Z" fill="#f6b800"/>
</svg>
<h2 class="abs serif day-title">Ein Tag bei uns.</h2>
<p class="abs day-sub">So sieht ein Tag in unserer Tagespflege aus.</p>
<div class="abs tl-line"></div>
<div class="tl" style="top:2180px"><div class="ic"><svg width="26" height="26" viewBox="0 0 24 24" fill="none" stroke="#fff" stroke-width="1.5"><path d="M5 10h12v4a5 5 0 01-5 5H10a5 5 0 01-5-5zM17 11h2a2 2 0 010 4h-2M9 4v3M13 4v3"/></svg></div>
  <div><h4>Morgens</h4><div class="t">Ankommen &amp; Frühstück</div><div class="s">In Gemeinschaft gut in den Tag starten.</div></div></div>
<div class="tl" style="top:2275px"><div class="ic"><svg width="28" height="28" viewBox="0 0 24 24" fill="none" stroke="#fff" stroke-width="1.4"><circle cx="12" cy="8" r="3"/><circle cx="5.5" cy="10" r="2.2"/><circle cx="18.5" cy="10" r="2.2"/><path d="M7 19a5 5 0 0110 0zM1.5 19a4 4 0 016-3.4M22.5 19a4 4 0 00-6-3.4"/></svg></div>
  <div><h4>Vormittag</h4><div class="t">Aktivitäten &amp; Bewegung</div><div class="s">Zeitung lesen, Bewegung, Spaziergänge und kreative Aktivitäten.</div></div></div>
<div class="tl" style="top:2380px"><div class="ic"><svg width="24" height="24" viewBox="0 0 24 24" fill="none" stroke="#fff" stroke-width="1.6"><path d="M8 3v18M5 3v5a3 3 0 006 0V3M16 21V3c2 0 3 3 3 7h-3"/></svg></div>
  <div><h4>Mittag</h4><div class="t">Gemeinsames Mittagessen</div><div class="s">In angenehmer Gemeinschaft.</div></div></div>
<div class="tl" style="top:2470px"><div class="ic"><svg width="26" height="26" viewBox="0 0 24 24" fill="none" stroke="#fff" stroke-width="1.5"><path d="M4 10h13v3a5 5 0 01-5 5H9a5 5 0 01-5-5zM17 11h2a2 2 0 010 4h-2M3 20h16"/></svg></div>
  <div><h4>Nachmittag</h4><div class="t">Ruhe &amp; Kaffeerunde</div><div class="s">Kaffee, Ruhe und Zeit zum Erzählen.</div></div></div>
<div class="abs fahr"><div class="serif" style="font-size:27px">Fahrdienst</div><div style="font-size:24px;font-weight:600;line-height:35px">Abholung &amp;<br>Rückfahrt</div></div>

<!-- Team -->
<h2 class="abs serif team-title">Menschen, denen<br>Sie vertrauen können.</h2>
<p class="abs team-lead">Unser engagiertes Team begleitet Sie mit Fachkompetenz, Fürsorge und Herz.</p>
<div class="btn btn-yellow" style="left:40px;top:2844px;width:220px;height:37px;padding-left:14px;font-size:12px">Unser Team kennenlernen <svg width="22" height="14" viewBox="0 0 22 14" fill="none" stroke="#1c1c1c" stroke-width="1.8"><path d="M1 7h19M14 1l6 6-6 6"/></svg></div>
<div class="member" style="left:374px"><div class="pic" style="background:linear-gradient(180deg,#d9d2c6,#b34a4a)" role="img" aria-label="Porträtfoto Karin Brenner"></div><h4>Karin Brenner</h4><div class="bar"></div><p>Managing Director</p></div>
<div class="member" style="left:629px"><div class="pic" style="background:linear-gradient(180deg,#e6e4e0,#4f6b8c)" role="img" aria-label="Porträtfoto Jonas Brenner"></div><h4>Jonas Brenner</h4><div class="bar"></div><p>Managing Director<br>/ 2nd Head of Nursing Services</p></div>
<div class="member" style="left:888px"><div class="pic" style="background:linear-gradient(180deg,#e3e4e2,#8cb5d6)" role="img" aria-label="Porträtfoto Petra Kühnel"></div><h4>Petra Kühnel</h4><div class="bar"></div><p>Nursing Service Management</p></div>

<!-- Thanks -->
<div class="photo" style="left:640px;top:3016px;width:560px;height:334px;background:linear-gradient(90deg,var(--cream) 0%,rgba(210,210,215,.6) 25%,#c9cfd6 60%,#b9a79a 100%)" role="img" aria-label="Foto: Älterer Herr mit Rollator wird von einer Pflegerin begleitet"></div>
<h2 class="abs serif thanks-title">Danksagung von Patienten</h2>
<div class="abs quote-mark">“</div>
<p class="abs thanks-text">Schwestern und Pfleger sind dort täglich bereit,<br>helfen Patienten zu jeder Zeit.<br>Die können so trotz Schwierigkeiten<br>ihr Leben immer noch bestreiten.</p>
<div class="abs script thanks-script">„Danke für die gute Pflege.“</div>
<div class="abs thanks-name">Gerda und Walter Hoffmann<small>Auszug aus einer Danksagung</small></div>

<!-- Questions -->
<svg class="abs" style="left:650px;top:3350px" width="550" height="334" viewBox="0 0 550 334">
  <defs><linearGradient id="askG" x1="0" y1="0" x2="1" y2="0"><stop offset="0" stop-color="#dfe3e7"/><stop offset=".6" stop-color="#6c88b0"/><stop offset="1" stop-color="#2c3f63"/></linearGradient></defs>
  <path d="M60 0 H550 V334 H50 C20 270 10 200 14 140 C18 80 34 30 60 0Z" fill="url(#askG)" role="img" aria-label="Foto: Pflegerin stützt eine Seniorin beim Gehen"/>
</svg>
<h2 class="abs serif ask-title">Sie haben Fragen?<em>Wir sind für Sie da.</em></h2>
<p class="abs ask-lead">Rufen Sie uns an, schreiben Sie uns oder<br>lassen Sie sich zurückrufen.</p>
<div class="ccard" style="left:60px"><div class="ic"><svg width="20" height="20" viewBox="0 0 24 24"><path d="M6.6 10.8a15 15 0 006.6 6.6l2.2-2.2a1 1 0 011-.25 11.4 11.4 0 003.6.57 1 1 0 011 1V20a1 1 0 01-1 1A17 17 0 013 4a1 1 0 011-1h3.5a1 1 0 011 1c0 1.25.2 2.45.57 3.57a1 1 0 01-.25 1z" fill="none" stroke="#6a6a6a" stroke-width="1.5"/></svg></div><div><b>Anrufen</b><span>0371 / 4590120</span><small>24h-Hotline</small></div></div>
<div class="ccard" style="left:274px"><div class="ic"><svg width="20" height="20" viewBox="0 0 24 24" fill="none" stroke="#6a6a6a" stroke-width="1.5"><path d="M6.6 10.8a15 15 0 006.6 6.6l2.2-2.2a1 1 0 011-.25 11.4 11.4 0 003.6.57 1 1 0 011 1V20a1 1 0 01-1 1A17 17 0 013 4a1 1 0 011-1h3.5a1 1 0 011 1c0 1.25.2 2.45.57 3.57a1 1 0 01-.25 1zM20 3l-6 6M14 4v5h5"/></svg></div><div><b>Rückruf anfordern</b><span>Wir rufen Sie<br>gerne zurück.</span></div></div>
<div class="ccard" style="left:487px"><div class="ic"><svg width="20" height="20" viewBox="0 0 24 24" fill="none" stroke="#6a6a6a" stroke-width="1.5"><rect x="3" y="5" width="18" height="14" rx="1"/><path d="M3 6l9 7 9-7"/></svg></div><div><b>Kontaktformular</b><span>Schreiben Sie uns<br>eine Nachricht.</span></div></div>

<!-- Footer -->
<div class="abs f-brand"></div>
<div class="abs serif f-name">Hauskranken- und<br>Tagespflege<br>„Am Lindenhof“</div>
<div class="abs script f-script">Pflege mit Respekt.<br>Betreuung mit Herz.</div>
<div class="abs f-small">Ihr Pflegeteam aus Chemnitz</div>
<div class="f-col" style="left:358px"><h5>Navigation</h5>
  <ul class="f-nav"><li>Über uns</li><li>Hauskrankenpflege</li><li>Tagespflege</li><li>Team</li><li>Kontakt</li></ul></div>
<div class="f-col" style="left:557px"><h5>Kontakt</h5>
  <div class="f-row" style="margin-top:32px"><div class="ic"><svg width="16" height="16" viewBox="0 0 24 24" fill="none" stroke="#6a6a6a" stroke-width="1.6"><path d="M12 21s-7-6-7-12a7 7 0 0114 0c0 6-7 12-7 12z"/><circle cx="12" cy="9" r="2.5"/></svg></div><div>Lindenstraße 24<br>09130 Chemnitz</div></div>
  <div class="f-row"><div class="ic"><svg width="15" height="15" viewBox="0 0 24 24"><path d="M6.6 10.8a15 15 0 006.6 6.6l2.2-2.2a1 1 0 011-.25 11.4 11.4 0 003.6.57 1 1 0 011 1V20a1 1 0 01-1 1A17 17 0 013 4a1 1 0 011-1h3.5a1 1 0 011 1c0 1.25.2 2.45.57 3.57a1 1 0 01-.25 1z" fill="none" stroke="#6a6a6a" stroke-width="1.6"/></svg></div><div style="padding-top:6px">0371 / 4590120</div></div>
  <div class="f-row"><div class="ic"><svg width="15" height="15" viewBox="0 0 24 24" fill="none" stroke="#6a6a6a" stroke-width="1.6"><rect x="3" y="5" width="18" height="14" rx="1"/><path d="M3 6l9 7 9-7"/></svg></div><div style="padding-top:6px;font-size:9px">info@pflege-am-lindenhof.de</div></div></div>
<div class="f-col" style="left:772px"><h5>Öffnungszeiten</h5>
  <div class="f-row" style="margin-top:32px;font-size:10px"><div class="ic"><svg width="15" height="15" viewBox="0 0 24 24" fill="none" stroke="#6a6a6a" stroke-width="1.6"><rect x="3" y="5" width="18" height="16" rx="2"/><path d="M3 10h18M8 3v4M16 3v4"/></svg></div>
  <div style="color:var(--teal)"><b>Mo – Do</b><br><span style="color:#1c1c1c">09:00 – 15:00 Uhr</span><br><br><b>Fr</b><br><span style="color:#1c1c1c">09:00 – 14:00 Uhr</span><br><br>und nach Vereinbarung</div></div></div>
<div class="abs hotline-box">
  <svg width="52" height="52" viewBox="0 0 24 24" fill="none" stroke="#0f4c57" stroke-width="1.4"><path d="M6.6 10.8a15 15 0 006.6 6.6l2.2-2.2a1 1 0 011-.25 11.4 11.4 0 003.6.57 1 1 0 011 1V20a1 1 0 01-1 1A17 17 0 013 4a1 1 0 011-1h3.5a1 1 0 011 1c0 1.25.2 2.45.57 3.57a1 1 0 01-.25 1zM15 3a6 6 0 016 6M15 6a3 3 0 013 3"/></svg>
  <div style="font-size:12px;font-weight:600;margin-top:12px">24h-Hotline</div>
  <div style="font-size:17px;font-weight:700;margin-top:14px">0371 / 4590120</div>
</div>

<div class="abs bottom">
  <span>© 2026 Hauskranken- und Tagespflege „Am Lindenhof“</span>
  <nav><span>Impressum</span><i></i><span>Datenschutz</span></nav>
</div>

</body>
</html>
```